Business card

We need a business card design for our company based in Auckland , New Zealand called 'Quill + Habitat Ltd'. We provide architectural services. We would like to see designs that use the max. three colours (such as white, black, grey) The final design should communicate financial safety and growth."
Also I will provide our company logo. I would like to the logo to be embeded onto our business card.

Target Market(s)

new residential house, alteration & addition & light commericila design & drafting service

Industry/Entity Type

Architecture

Contact Information for Business Card

Company name: quill + habitat Ltd.
Name: Rowan Teale
Job title: architectural designer & Design QWR
email address: rowan@qandh.co.nz
mobile number: 02 5136 2297
web site: www.qandh.co.nz

Requirements
Must have
• My project must have..
• - embeded logo (attached company logo)
• I don't have a bigger version for our company logo, but I have one old one, so you can remove the word from it)
• - insert the attached small GVTK logo & QWR logo
• - creative, simple and clear business card.
• - Max. three colours
Nice to have
• - Here are the samples I would like to share with you: http://www.velmoriq.com/blog/sparse-stationery-layouts/
• I would like to have my business card like one of the creation.
Should not have
• TBA

```html
<!DOCTYPE html>
<html lang="en">
<head>
<meta charset="utf-8">
<title>Quill + Habitat Ltd — Business Card</title>
<link rel="stylesheet" href="https://fonts.googleapis.com/css2?family=Ubuntu:wght@300;400;500&display=swap">
<style>
  :root {
    --backdrop: #e4e6e9;
    --card: #ffffff;
    --ink: #111111;
    --muted: #8a8a8a;
    --mark-tone: #d9d9d9;
  }
  html, body {
    margin: 0;
    width: 1200px;
    height: 900px;
    overflow: hidden;
    background: var(--backdrop);
    font-family: "Ubuntu", sans-serif;
  }
  .card {
    position: absolute;
    left: 150px;
    top: 190px;
    width: 900px;
    height: 520px;
    background: var(--card);
    box-shadow: 0 10px 30px rgba(0,0,0,0.12);
    color: var(--ink);
  }
  .brand-decoration {
    position: absolute;
    left: 380px;
    top: 30px;
    width: 280px;
    height: 210px;
    background: radial-gradient(circle at 55% 45%, var(--mark-tone), #f6f6f6 70%);
  }
  .membership-badges {
    position: absolute;
    left: 690px;
    top: 160px;
    display: flex;
    gap: 18px;
    align-items: flex-end;
  }
  .badge-circle {
    width: 74px;
    height: 74px;
    border-radius: 50%;
    background: var(--ink);
  }
  .badge-square {
    width: 58px;
    height: 58px;
    background: var(--muted);
  }
  .divider {
    position: absolute;
    left: 470px;
    right: 0;
    top: 256px;
    height: 2px;
    background: var(--ink);
  }
  .company-name {
    position: absolute;
    left: 56px;
    top: 290px;
    margin: 0;
    font-size: 26px;
    font-weight: 500;
    letter-spacing: -0.3px;
    line-height: 1.1;
  }
  .person {
    position: absolute;
    left: 56px;
    top: 345px;
  }
  .person-name {
    margin: 0;
    font-size: 30px;
    font-weight: 300;
    line-height: 1.1;
  }
  .person-title {
    margin: 4px 0 0;
    font-size: 16px;
    font-weight: 300;
    color: var(--muted);
  }
  .contact {
    position: absolute;
    left: 56px;
    top: 418px;
    margin: 0;
    font-size: 15px;
    font-weight: 400;
    line-height: 1.35;
  }
</style>
</head>
<body>
  <article class="card">
    <div class="brand-decoration" role="img" aria-label="Large decorative brand symbol"></div>

    <div class="membership-badges">
      <div class="badge-circle" role="img" aria-label="Licensed practitioner badge"></div>
      <div class="badge-square" role="img" aria-label="GVTK professional member badge"></div>
    </div>

    <div class="divider"></div>

    <p class="company-name">quill + habitat Ltd.</p>

    <div class="person">
      <p class="person-name">Rowan Teale</p>
      <p class="person-title">Architectural designer &amp; Design QWR</p>
    </div>

    <p class="contact">
      02 5136 2297<br>
      rowan@qandh.co.nz<br>
      www.qandh.co.nz
    </p>
  </article>
</body>
</html>
```